Brassmoor Yard UK needs Street Markets Brochure

We need a brochure to market our street market festival.

Established over 250 years ago based in the heart if the UK the brassmoor yard is home to the biggest jewellery district in the EU.

The street market festival will be held with the view of boosting tourism numbers to the area with a host of markets and initiatives based around the area on a designated monthly day.

We would like to the the design in both a4 and a5 and the we will make a decision as to which look the best - the designer will have to take into consideration the bleed margin for print purposes.

The designer will be given creative control over the imagery used and these should be relevant to the subject matter. We will purchase the relevant images if they are selected from pixlane etc but they should encompass a fun and happy vibe if people are used.

Designer please design project using Adobe InDesign and send final winning files in this format.

Reason: The designs so far are not as challenging or upto the quality we would of hoped for. Please could you refer to the brief and enhance the quality of the brochure designs.

Reason: We have conducted a poll and have decided to extend the competition a further 5 days. The reason being a) We would like a design that can be picked up wherever it is left e.g. Hotels, Train Stations b) A design that can be utilized around the year in all seasons We will be increasing the budget for the project and invite new or reassessed designs Thanks

Target Market(s)

International Tourist, Local Business Community, Regional Community, Couples,
Mature Adults, OAP's

Industry/Entity Type

Tourism

Font styles to use
Sans Serif

Requirements
Must have
• Relevant imagery, vibrant professionally design
• Designer please read brief to get a grasp of the area and what is needed - brochure must attract readers both online version and hand version.
Nice to have
• Imagery that takes the reader to the area and causes curiosity to visit to find out what is happening.
• A image of Thornwick should be used to describe the street performance area.
Should not have
• Irrelevant imagery

```html
<!DOCTYPE html>
<html lang="en">
<head>
<meta charset="utf-8">
<title>Brassmoor Yard Street Markets Brochure</title>
<link rel="stylesheet" href="https://fonts.googleapis.com/css2?family=Poppins:wght@600;700&family=Mulish:wght@400;600&family=Kalam&display=swap">
<style>
  :root {
    --orange: #e8592a;
    --orange-text: #de5524;
    --green: #7dbf3a;
    --green-title: #78bd3f;
    --page: #efefef;
    --page-edge: #e2e2e2;
    --backdrop: #d9d9d9;
  }
  * { box-sizing: border-box; margin: 0; padding: 0; }
  html, body { width: 1200px; height: 847px; overflow: hidden; }
  body {
    background: var(--backdrop);
    font-family: "Mulish", sans-serif;
    position: relative;
  }
  .spread {
    position: absolute; left: 30px; top: 30px; width: 1140px; height: 787px;
    display: flex; box-shadow: 0 6px 24px rgba(0,0,0,.18);
  }
  .page {
    position: relative; width: 570px; height: 787px; overflow: hidden;
    background: linear-gradient(180deg, var(--page) 0%, #f6f6f6 50%, var(--page) 100%);
  }
  .page--left { border-right: 1px solid var(--page-edge); }
  .band { position: absolute; left: 0; width: 570px; height: 64px; display: block; }
  .band--top { top: 0; }
  .band--bottom { bottom: 0; }
  .photo { position: absolute; box-shadow: 0 2px 6px rgba(0,0,0,.25); }
  .title {
    position: absolute; font-family: "Poppins", sans-serif; font-weight: 700;
    color: var(--green-title); text-transform: uppercase; line-height: 1.05;
    letter-spacing: .5px; white-space: nowrap;
  }
  .title--lg { font-size: 30px; }
  .title--md { font-size: 22px; }
  .title--right { text-align: right; }
  .rule { position: absolute; height: 1.5px; background: var(--orange); }
  .copy {
    position: absolute; color: var(--orange-text); font-size: 11.5px; line-height: 1.4;
  }
  .copy--lg { font-size: 12.5px; }
  .featuring { font-family: "Poppins", sans-serif; font-weight: 600; font-size: 14px; display: block; margin-top: 4px; }
  .notes {
    position: absolute; left: 15px; top: 565px; width: 118px; height: 128px;
    background: linear-gradient(180deg, #f2f2f2, #d8d8d8); border: 1px solid #bdbdbd;
    padding: 8px 8px; font-family: "Kalam", cursive; color: #c0262d;
  }
  .notes__head { font-size: 12px; font-weight: 400; }
  .notes__body { font-size: 7.5px; line-height: 1.35; margin-top: 2px; }
  .notes__mail { font-size: 7.5px; margin-top: 3px; }
  .notes__icon { position: absolute; left: 38px; bottom: 10px; }
</style>
</head>
<body>
<main class="spread">

  <section class="page page--left">
    <svg class="band band--top" viewBox="0 0 570 64" preserveAspectRatio="none" aria-hidden="true">
      <polygon points="0,38 570,0 570,6 0,50" fill="var(--orange)"/>
      <path d="M0,54 C200,48 380,20 570,8 L570,14 C380,28 200,54 0,60 Z" fill="var(--green)"/>
    </svg>

    <div class="photo" role="img" aria-label="Close-up of a jewelled vintage brooch" style="left:290px;top:70px;width:245px;height:110px;background:radial-gradient(circle at 50% 50%,#b89a62 0%,#4a3d2a 40%,#111 80%);"></div>
    <h2 class="title title--lg title--right" style="left:15px;top:100px;width:265px;">Antiques Fair</h2>
    <div class="rule" style="left:15px;top:140px;width:270px;"></div>
    <p class="copy" style="left:15px;top:145px;width:270px;">Antique &amp; Collectors Fair with antiques, collectables, fine and vintage jewellery, linens, silver, metalware, militia memorabilia and lots lots more</p>

    <div class="photo" role="img" aria-label="Collage of local landmarks, red phone boxes and street views" style="left:15px;top:225px;width:205px;height:135px;background:linear-gradient(135deg,#7fa6c9 0%,#b5523f 45%,#c9372c 65%,#8a8f96 100%);"></div>
    <h2 class="title title--lg" style="left:235px;top:232px;">Area Tours</h2>
    <div class="rule" style="left:235px;top:270px;width:320px;"></div>
    <p class="copy" style="left:235px;top:274px;width:320px;">Let the experts show you the real Brassmoor Yard with these guided tours that delve into the area's history, landmarks, emerging culture and much more</p>

    <div class="photo" role="img" aria-label="Colourful painted portrait artwork" style="left:310px;top:385px;width:245px;height:128px;background:radial-gradient(circle at 50% 50%,#c87a4a 0%,#6f7a2e 45%,#2b3320 100%);"></div>
    <h2 class="title title--lg title--right" style="left:15px;top:413px;width:285px;">Art Fair</h2>
    <div class="rule" style="left:15px;top:451px;width:285px;"></div>
    <p class="copy" style="left:15px;top:456px;width:285px;">Visitors can view and buy art from an assortment of galleries and artists presenting collections of visual art, photography, sculpture, glass work and ceramics</p>

    <div class="photo" role="img" aria-label="Clothes rails and shelves in a market stall" style="left:15px;top:560px;width:210px;height:170px;background:linear-gradient(160deg,#d9d2c4 0%,#8c6e4e 45%,#3a3f57 75%,#b89a6a 100%);"></div>
    <h2 class="title title--lg" style="left:240px;top:560px;">Clothes Market</h2>
    <div class="rule" style="left:240px;top:598px;width:318px;"></div>
    <p class="copy copy--lg" style="left:240px;top:603px;width:318px;">If you're looking for designer brands at discount prices, on a budget, or looking for something different to the usual high street fashions, a trip to our clothes markets is sure to provide you with inspiration. Shop for unique and unusual clothes, plus vintage threads and second-hand treasures at our clothes market.</p>

    <svg class="band band--bottom" viewBox="0 0 570 64" preserveAspectRatio="none" aria-hidden="true">
      <path d="M0,64 L0,52 C200,46 400,20 570,6 L570,64 Z" fill="var(--orange)"/>
      <path d="M0,48 C200,40 400,12 570,0 L570,5 C400,18 200,44 0,52 Z" fill="var(--green)"/>
    </svg>
  </section>

  <section class="page page--right">
    <svg class="band band--top" viewBox="0 0 570 64" preserveAspectRatio="none" aria-hidden="true">
      <polygon points="0,48 570,0 570,10 0,56" fill="var(--orange)"/>
      <path d="M0,58 C200,52 380,26 570,14 L570,20 C380,34 200,58 0,62 Z" fill="var(--green)"/>
    </svg>

    <div class="photo" role="img" aria-label="Row of craft beer bottles" style="left:15px;top:72px;width:165px;height:110px;background:linear-gradient(90deg,#a8531c 0%,#d99a3a 30%,#7a3b12 55%,#c98a2e 80%,#5b2d10 100%);"></div>
    <h2 class="title title--md" style="left:195px;top:78px;">Craft Beer Tent</h2>
    <div class="rule" style="left:195px;top:104px;width:360px;"></div>
    <p class="copy" style="left:195px;top:108px;width:360px;">An extraordinary experience featuring specialty craft beers from craft breweries from throughout the midlands and UK</p>

    <div class="photo" role="img" aria-label="Silver rings and bangles on red fabric" style="left:330px;top:150px;width:225px;height:110px;background:radial-gradient(circle at 45% 55%,#e6d9dc 0%,#c8102e 40%,#7a0a1d 100%);"></div>
    <h2 class="title title--md title--right" style="left:15px;top:192px;width:300px;">Jewellery Fair</h2>
    <div class="rule" style="left:15px;top:218px;width:300px;"></div>
    <p class="copy" style="left:15px;top:222px;width:300px;">Browse a stunning collection and unrivalled choice of contemporary jewellery and stylish silverware. Visitors can purchase from an exciting range by local, emerging British talent as well as the latest designs from more established makers.</p>

    <div class="photo" role="img" aria-label="Plates of street food with a fruit drink" style="left:15px;top:312px;width:195px;height:165px;background:linear-gradient(150deg,#3f8a2e 0%,#f0c070 40%,#d9582a 65%,#f3efe6 100%);"></div>
    <h2 class="title title--md" style="left:225px;top:310px;">Brassmoor Yard<br>Street Feast</h2>
    <div class="rule" style="left:225px;top:360px;width:330px;"></div>
    <p class="copy" style="left:225px;top:364px;width:330px;">Brings together a wide variety of street food cultures from around the globe creating a unique dining experience that will leave attendees licking their lips and fingers for more.
      <span class="featuring">Featuring:</span>
      Tacos, Jerk, Curries, Burgers, Burritos, Brownies, Fries, Stews, Pizzas, Sausages, Slow Roasts, Pulled Meats, Wraps, Noodles, Desserts, Shakes...</p>

    <div class="photo" role="img" aria-label="Engraved portrait of the playwright Thornwick" style="left:365px;top:500px;width:190px;height:190px;background:radial-gradient(circle at 50% 40%,#9a9a9a 0%,#4a4a4a 55%,#1e1e1e 100%);"></div>
    <h2 class="title title--md title--right" style="left:15px;top:502px;width:340px;">Thornwick Street<br>Performers</h2>
    <div class="rule" style="left:15px;top:553px;width:340px;"></div>

    <aside class="notes">
      <p class="notes__head">Notes:</p>
      <p class="notes__body">If you would like to get involved with any of the above areas as a trader then please email with a brief of your area of preference.</p>
      <p class="notes__mail">stalls@brassmooryard.tv</p>
      <svg class="notes__icon" width="40" height="26" viewBox="0 0 40 26" aria-hidden="true">
        <rect x="0" y="0" width="40" height="26" fill="#c0262d"/>
        <polyline points="1,1 20,15 39,1" fill="none" stroke="#f2f2f2" stroke-width="2"/>
      </svg>
    </aside>

    <p class="copy" style="left:145px;top:562px;width:212px;">Come and enjoy a variety of Thornwick plays either on our Thornwick stage or specially adapted performances adapted by our team of Street Performers who will perform to large circles of people. They are capable of entertaining crowds hundreds strong for 45 minutes with a combination of adapted scripts and comedy inserts.</p>
  </section>

</main>
</body>
</html>
```